Fresh Nest Builder Guide needs a new Landing Page

I like to get a landing page or website with 2-3 pages to help target home buyers who are looking to buy homes from builders such as PV Dwellings, Moritz, G.T. Falwick, etc. The landing page/website to be non-cluttered and be able to explain to home buyers that there are many benefits to include me as their buyer's agent when they buy a brand new home from any builders.
I may want to incorporate a short explanation video (animated) on the landing page and then for the viewer to click on a button that will take them to another page where they can search for new homes from different builders.
Target Market(s)
Home buyers looking to buy brand new home from builders such as PV Dwellings, Moritz, G.T. Falwick, etc.
Industry/Entity Type
Real Estate
Number of Pages Required
2 page
Requirements
Must have
- The landing page may have the explanation video at the bottom of the landing page (scrolled down) or there may be a CALL TO ACTION button that takes the viewer to the 2nd page to watch the explanation video. Once they watched the explanation video and are still interested, they can click on another CALL TO ACTION button that will take them to another website that they will be able to search for all the available new homes and register their contact information.
Should not have
- No clutters and no dark colors.

```html
<!DOCTYPE html>
<html lang="en">
<head>
<meta charset="utf-8">
<title>Fresh Nest Builder Guide</title>
<link rel="stylesheet" href="https://fonts.googleapis.com/css2?family=Open+Sans:wght@400;600;700&display=swap">
<style>
:root{
  --white:#ffffff;
  --ink:#333333;
  --muted:#777777;
  --line:#cccccc;
  --accent-red:#b3282d;
  --accent-orange:#e8875a;
  --card-dark:#2d2d2d;
  --footer:#262626;
  --sky-top:#4f93d6;
  --sky-low:#9cc6ea;
  --hill:#3c5d3a;
}
*{box-sizing:border-box;margin:0;padding:0}
html,body{width:703px;height:1200px;overflow:hidden;background:var(--white);font-family:"Open Sans",Arial,sans-serif;color:var(--ink)}
.page{position:relative;width:703px;height:1200px}

.site-nav{height:33px;display:flex;justify-content:center;align-items:center;gap:22px;font-size:8px;letter-spacing:.8px;color:var(--muted);background:var(--white)}
.site-nav a{color:inherit;text-decoration:none}
.site-nav a.active{color:#bbb}

.hero{position:relative;height:377px;background:linear-gradient(180deg,var(--sky-top) 0%,var(--sky-low) 45%,#6f8fa8 55%,var(--hill) 72%,#6d6a4e 100%);text-align:center;color:var(--white)}
.hero-kicker{position:absolute;top:132px;width:100%;font-size:8px;letter-spacing:1px;text-transform:uppercase}
.hero-title{position:absolute;top:142px;width:100%;font-size:30px;font-weight:400;color:var(--accent-red)}
.hero-sub{position:absolute;top:192px;left:190px;width:323px;font-size:8px;line-height:12px}
.hero-btn{position:absolute;top:220px;left:294px;width:115px;height:25px;border-radius:13px;background:var(--accent-orange);color:var(--white);font-size:9px;line-height:25px}

.section-title{position:absolute;top:424px;width:100%;text-align:center;font-size:19px;font-weight:400}
.section-rule{position:absolute;top:455px;left:336px;width:30px;height:1px;background:var(--line)}

.video{position:absolute;left:122px;top:485px;width:342px;height:230px;border-radius:4px;overflow:hidden;background:linear-gradient(160deg,#1b1a24 0%,#4a2e1d 45%,#c36a2a 70%,#1f2a3a 100%)}
.video-caption{position:absolute;top:130px;width:100%;text-align:center;color:var(--white);font-size:16px}
.video-price{position:absolute;top:155px;width:100%;text-align:center;color:var(--white);font-size:28px;font-weight:700}
.video-bar{position:absolute;bottom:0;left:0;width:100%;height:18px;background:rgba(0,0,0,.6)}
.video-progress{position:absolute;bottom:16px;left:0;width:100%;height:2px;background:#777}

.badge{position:absolute;left:481px;top:510px;width:80px;height:80px;border-radius:50%;background:linear-gradient(135deg,#d9f0d2,#6cbf4f)}
.badge-caption{position:absolute;left:556px;top:580px;font-size:5px;color:var(--muted)}
.side-photo{position:absolute;left:475px;top:605px;width:106px;height:105px;background:linear-gradient(180deg,#3d8ed8,#8fc6e6 50%,#2f7a3c)}

.house-photo{position:absolute;left:122px;top:722px;width:223px;height:185px;background:linear-gradient(180deg,#8fb4d6 0%,#cfd8df 45%,#e9eef1 60%,#35475a 100%)}

.enquiry{position:absolute;left:368px;top:728px;width:218px;font-size:6px;color:var(--ink)}
.enquiry h3{font-size:7px;font-weight:700;margin-bottom:8px}
.field-row{display:flex;gap:10px;margin-bottom:6px}
.field{flex:1}
.field label{display:block;margin-bottom:2px}
.field .input{height:10px;border:1px solid var(--line)}
.field .textarea{height:42px;border:1px solid var(--line)}
.submit{margin-top:8px;width:42px;height:10px;border:1px solid var(--line);font-size:5px;text-align:center;line-height:8px}

.cards{position:absolute;top:937px;left:117px;display:flex;gap:14px}
.card{width:146px;height:188px;background:var(--card-dark);color:var(--white);text-align:center}
.card.highlight{background:var(--accent-orange)}
.card-photo{height:90px}
.card-kicker{margin-top:8px;font-size:6px;color:#bbb}
.card.highlight .card-kicker{color:#fbe0d2}
.card-title{font-size:15px;font-weight:400;margin-top:2px}
.card-rule{width:24px;height:1px;background:#888;margin:6px auto}
.card-text{font-size:6px;line-height:9px;padding:0 18px}

.site-footer{position:absolute;bottom:0;left:0;width:703px;height:47px;background:var(--footer);color:#bbb;font-size:6px;display:flex;justify-content:space-between;align-items:center;padding:0 120px}
</style>
</head>
<body>
<div class="page">
  <nav class="site-nav">
    <a class="active" href="#">HOME</a><a href="#">ABOUT</a><a href="#">PORTFOLIO</a><a href="#">PRICING</a><a href="#">CONTACT</a>
  </nav>

  <header class="hero" role="img" aria-label="Hillside home above a lake with mountains and blue sky">
    <p class="hero-kicker">Premium Investments</p>
    <h1 class="hero-title">Awesome Designer Properties</h1>
    <p class="hero-sub">Buy a brand new home from top builders with a buyer's agent on your side, at no extra cost to you.</p>
    <div class="hero-btn">Visit Properties</div>
  </header>

  <h2 class="section-title">Featured Properties</h2>
  <div class="section-rule"></div>

  <div class="video" role="img" aria-label="Explanation video frame showing a lit luxury home at dusk">
    <p class="video-caption">HOW MUCH TO CHARGE FOR REAL ESTATE?</p>
    <p class="video-price">$1,500 - $2,500</p>
    <div class="video-progress"></div>
    <div class="video-bar">
      <svg width="60" height="18" viewBox="0 0 60 18"><path d="M8 5 L14 9 L8 13 Z" fill="#fff"/><path d="M20 5 L25 9 L20 13 Z M26 5 h2 v8 h-2 Z" fill="#fff"/></svg>
    </div>
  </div>

  <div class="badge" role="img" aria-label="Certification badge"></div>
  <span class="badge-caption">Certified</span>
  <div class="side-photo" role="img" aria-label="Green plant growing under blue sky"></div>

  <div class="house-photo" role="img" aria-label="Modern white villa with pool reflection"></div>

  <form class="enquiry">
    <h3>Make Enquiry</h3>
    <div class="field-row">
      <div class="field"><label>First Name</label><div class="input"></div></div>
      <div class="field"><label>Last Name</label><div class="input"></div></div>
    </div>
    <div class="field-row">
      <div class="field"><label>Email</label><div class="input"></div></div>
      <div class="field"><label>Phone</label><div class="input"></div></div>
    </div>
    <div class="field-row">
      <div class="field"><label>Customer Message</label><div class="textarea"></div></div>
    </div>
    <div class="submit">Submit</div>
  </form>

  <div class="cards">
    <div class="card">
      <div class="card-photo" role="img" aria-label="Handshake over a house model" style="background:linear-gradient(180deg,#2f6fb0,#9fb8d4)"></div>
      <p class="card-kicker">About us</p>
      <h3 class="card-title">Meet the team</h3>
      <div class="card-rule"></div>
      <p class="card-text">Lorem ipsum dolor sit amet, consectetur adipiscing elit sed diam.</p>
    </div>
    <div class="card">
      <div class="card-photo" role="img" aria-label="Coin stacks with green sprouts" style="background:linear-gradient(180deg,#5b8f3a,#c9a24a)"></div>
      <p class="card-kicker">Portfolio</p>
      <h3 class="card-title">See our work</h3>
      <div class="card-rule"></div>
      <p class="card-text">Lorem ipsum dolor sit amet, consectetur adipiscing elit sed diam.</p>
    </div>
    <div class="card highlight">
      <div class="card-photo" role="img" aria-label="Small house model on green grass" style="background:linear-gradient(180deg,#cfe6f2,#5fa043)"></div>
      <p class="card-kicker">Contact</p>
      <h3 class="card-title">Work with us</h3>
      <div class="card-rule"></div>
      <p class="card-text">Lorem ipsum dolor sit amet, consectetur adipiscing elit sed diam.</p>
    </div>
  </div>

  <footer class="site-footer">
    <span>Copyright 2016 Real Estate. All Rights Reserved</span>
    <span>Privacy Policy &nbsp;|&nbsp; Terms &amp; Conditions</span>
  </footer>
</div>
</body>
</html>
```